Commercial Real Estate

We need a business card design for a new commercial real estate business that specializes in apartment building brokerage. Not individual units but the entire complex. We find and represent the owners existing buildings and well as new buyers for those buildings. The design should convey trust, integrity, knowledge and growth. It should be easily read.

Target Market(s)

40 to 65 years old

Industry/Entity Type

Real Estate

```html
<!DOCTYPE html>
<html lang="en">
<head>
<meta charset="utf-8">
<title>Keystead Realty Partners – Business Card</title>
<link href="https://fonts.googleapis.com/css2?family=Aldrich&display=swap" rel="stylesheet">
<style>
  :root{
    --teal:#6fc9c7;
    --teal-deep:#4fb3b0;
    --band:#5a6b6b;
    --paper:#ffffff;
    --paper-shade:#f1f2f2;
    --ink:#2f3535;
    --stage:#e8e6e2;
  }
  *{margin:0;padding:0;box-sizing:border-box}
  html,body{width:1200px;height:1019px;overflow:hidden}
  body{
    background:var(--stage);
    font-family:"Aldrich",sans-serif;
    color:var(--ink);
    display:flex;align-items:center;justify-content:center;gap:60px;
  }
  .card{
    width:500px;height:860px;position:relative;overflow:hidden;
    box-shadow:0 10px 30px rgba(0,0,0,.18);
  }
  .card-front{
    background:linear-gradient(180deg,var(--paper) 0%,var(--paper-shade) 100%);
  }
  .card-front::before,.card-front::after{
    content:"";position:absolute;top:0;bottom:0;width:24px;background:var(--teal);
  }
  .card-front::before{left:0}
  .card-front::after{right:0}
  .card-back{background:var(--teal)}

  .brand{
    position:absolute;top:170px;left:0;right:0;
    display:flex;flex-direction:column;align-items:center;gap:18px;
  }
  .brand-mark{width:56px;height:56px;background:var(--teal)}
  .brand-name{
    font-size:30px;letter-spacing:3px;color:var(--band);text-align:center;line-height:1.3;
  }
  .brand-rule{width:280px;height:2px;background:var(--teal)}

  .name-band{
    position:absolute;top:370px;left:0;right:0;height:118px;
    background:var(--band);color:var(--paper);
    display:flex;flex-direction:column;align-items:center;justify-content:center;gap:8px;
  }
  .person-name{font-size:32px;letter-spacing:3px}
  .person-title{font-size:24px;letter-spacing:3px}

  .contact-list{
    position:absolute;top:540px;left:44px;list-style:none;
    display:flex;flex-direction:column;gap:14px;
  }
  .contact-item{display:flex;align-items:center;gap:16px;font-size:17px;letter-spacing:.5px}
  .contact-icon{
    width:32px;height:32px;border-radius:5px;background:var(--teal);
    display:flex;align-items:center;justify-content:center;flex:none;
  }
  .contact-icon svg{width:18px;height:18px;fill:none;stroke:var(--paper);stroke-width:2;stroke-linecap:round;stroke-linejoin:round}
</style>
</head>
<body>
  <section class="card card-front">
    <div class="brand">
      <span class="brand-mark"></span>
      <p class="brand-name">KEYSTEAD<br>REALTY PARTNERS</p>
      <span class="brand-rule"></span>
    </div>

    <div class="name-band">
      <p class="person-name">DANIEL REEVE</p>
      <p class="person-title">GENERAL MANAGER</p>
    </div>

    <ul class="contact-list">
      <li class="contact-item">
        <span class="contact-icon"><svg viewBox="0 0 24 24"><path d="M5 3h4l2 5-3 2a11 11 0 0 0 6 6l2-3 5 2v4a2 2 0 0 1-2 2A17 17 0 0 1 3 5a2 2 0 0 1 2-2z"/></svg></span>
        <span>014 552 0187</span>
      </li>
      <li class="contact-item">
        <span class="contact-icon"><svg viewBox="0 0 24 24"><rect x="7" y="2" width="10" height="20" rx="2"/><path d="M11 18h2"/></svg></span>
        <span>014 552 0188</span>
      </li>
      <li class="contact-item">
        <span class="contact-icon"><svg viewBox="0 0 24 24"><path d="M7 8V3h10v5"/><rect x="3" y="8" width="18" height="9" rx="1"/><path d="M7 14h10v7H7z"/></svg></span>
        <span>014 552 0189</span>
      </li>
      <li class="contact-item">
        <span class="contact-icon"><svg viewBox="0 0 24 24"><rect x="3" y="5" width="18" height="14" rx="1"/><path d="M3 6l9 7 9-7"/></svg></span>
        <span>dreeve@keystead.com</span>
      </li>
      <li class="contact-item">
        <span class="contact-icon"><svg viewBox="0 0 24 24"><circle cx="12" cy="12" r="9"/><path d="M3 12h18M12 3c3 3 3 15 0 18M12 3c-3 3-3 15 0 18"/></svg></span>
        <span>www.keysteadrealty.com</span>
      </li>
      <li class="contact-item">
        <span class="contact-icon"><svg viewBox="0 0 24 24"><path d="M12 22s7-7 7-12a7 7 0 0 0-14 0c0 5 7 12 7 12z"/><circle cx="12" cy="10" r="2.5"/></svg></span>
        <span>41, 12th floor, Harbor Crest Avenue KLT</span>
      </li>
    </ul>
  </section>

  <section class="card card-back" aria-label="Card reverse side"></section>
</body>
</html>
```